Business Card and Stationary for Commercial Real Estate Brokerage
Tarvel Commercial
Business Card and Stationary for Commercial Real Estate Brokerage - Real Estate
Creative Brief
Use specific fonts
Use same as logo font or other, whichever looks best
Professional
Dorian P. Lusk
Senior Vice President
4821 Halbrook Avenue, Newport Beach, CA 92660
dlusk@tarvelpx.example
www.tarvelpx.example
CA DRE: 04263918
Please include additional business location with the following address and contact information in no particular order, as a placeholder: 318 Quillan Avenue, New York, NY 10166 Phone: 347-555-0192 License No. NY DRE: 86420913

```html
<!DOCTYPE html>
<html lang="en">
<head>
<meta charset="utf-8">
<title>Tarvel Commercial – Business Cards</title>
<link href="https://fonts.googleapis.com/css2?family=Montserrat:wght@400;600;700&display=swap" rel="stylesheet">
<style>
  :root {
    --backdrop: #e9ebef;
    --card: #ffffff;
    --brand-blue: #1d3f9e;
    --brand-deep: #102a72;
    --brand-bright: #2f6fe0;
    --ink: #4a4f5a;
    --ink-soft: #7a808c;
  }
  * { margin: 0; padding: 0; box-sizing: border-box; }
  html, body { width: 1200px; height: 629px; overflow: hidden; }
  body {
    background: var(--backdrop);
    font-family: "Montserrat", sans-serif;
    position: relative;
  }
  .card {
    position: absolute;
    top: 166px;
    width: 520px;
    height: 297px;
    background: var(--card);
    box-shadow: 0 6px 18px rgba(20, 30, 60, 0.15);
    overflow: hidden;
  }
  .card--back { left: 50px; }
  .card--front { left: 630px; }

  .wordmark {
    color: var(--brand-blue);
    font-weight: 700;
    letter-spacing: 1px;
    display: flex;
    align-items: center;
    gap: 10px;
    justify-content: center;
  }
  .wordmark__mark {
    width: 14px; height: 14px;
    background: var(--brand-blue);
  }
  .card--back .wordmark {
    position: absolute;
    top: 50%; left: 0; right: 0;
    transform: translateY(-50%);
    font-size: 34px;
  }
  .card--front .wordmark {
    position: absolute;
    top: 34px; left: 0; right: 0;
    font-size: 26px;
  }

  .person {
    position: absolute;
    top: 96px; left: 0; right: 0;
    text-align: center;
  }
  .person__name {
    font-size: 14px; font-weight: 600;
    color: var(--brand-blue);
    letter-spacing: 0.5px;
  }
  .person__title {
    font-size: 9px;
    color: var(--ink-soft);
    margin-top: 3px;
    letter-spacing: 0.5px;
  }

  .offices {
    position: absolute;
    top: 150px; left: 40px;
    width: 210px;
    font-size: 8.5px;
    line-height: 1.55;
    color: var(--ink);
  }
  .office + .office { margin-top: 8px; }
  .office__label { color: var(--brand-blue); font-weight: 600; }

  .contacts {
    position: absolute;
    top: 150px; left: 290px;
    list-style: none;
    font-size: 8.5px;
    color: var(--ink);
  }
  .contacts li {
    display: flex; align-items: center;
    gap: 7px;
    height: 16px;
  }
  .contact-icon {
    width: 11px; height: 11px;
    border-radius: 50%;
    background: var(--brand-blue);
    display: flex; align-items: center; justify-content: center;
  }

  .swoosh {
    position: absolute;
    left: 0; bottom: 0;
    width: 520px; height: 70px;
  }
  .swoosh__url {
    position: absolute;
    left: 40px; bottom: 10px;
    font-size: 8px;
    letter-spacing: 2px;
    color: #ffffff;
  }
</style>
</head>
<body>

  <section class="card card--back" aria-label="Business card back">
    <div class="wordmark"><span class="wordmark__mark"></span>Tarvel Commercial</div>
  </section>

  <section class="card card--front" aria-label="Business card front">
    <div class="wordmark"><span class="wordmark__mark"></span>Tarvel Commercial</div>

    <div class="person">
      <div class="person__name">Dorian P. Lusk</div>
      <div class="person__title">Senior Vice President</div>
    </div>

    <div class="offices">
      <div class="office">
        4821 Halbrook Avenue<br>
        Newport Beach, CA 92660<br>
        <span class="office__label">CA DRE:</span> 04263918
      </div>
      <div class="office">
        318 Quillan Avenue<br>
        New York, NY 10166<br>
        <span class="office__label">NY DRE:</span> 86420913
      </div>
    </div>

    <ul class="contacts">
      <li>
        <span class="contact-icon">
          <svg width="7" height="7" viewBox="0 0 10 10"><rect x="1" y="2.5" width="8" height="5.5" fill="none" stroke="#fff" stroke-width="1.2"/><path d="M1 2.5 L5 6 L9 2.5" fill="none" stroke="#fff" stroke-width="1.2"/></svg>
        </span>
        dlusk@tarvelpx.example
      </li>
      <li>
        <span class="contact-icon">
          <svg width="7" height="7" viewBox="0 0 10 10"><path d="M2.5 1 L4 1 L4.6 3.4 L3.6 4.2 Q4.5 6 5.8 6.6 L6.6 5.6 L9 6.2 L9 7.8 Q8.5 9 7 9 Q1 8 1 2.5 Q1 1 2.5 1 Z" fill="#fff"/></svg>
        </span>
        347-555-0192
      </li>
      <li>
        <span class="contact-icon">
          <svg width="7" height="7" viewBox="0 0 10 10"><path d="M5 0.8 A3 3 0 0 1 8 3.8 Q8 6 5 9.4 Q2 6 2 3.8 A3 3 0 0 1 5 0.8 Z" fill="#fff"/><circle cx="5" cy="3.8" r="1.1" fill="#1d3f9e"/></svg>
        </span>
        Newport Beach &amp; New York
      </li>
      <li>
        <span class="contact-icon">
          <svg width="7" height="7" viewBox="0 0 10 10"><circle cx="5" cy="5" r="3.8" fill="none" stroke="#fff" stroke-width="1.1"/><path d="M1.2 5 H8.8 M5 1.2 Q2.8 5 5 8.8 M5 1.2 Q7.2 5 5 8.8" fill="none" stroke="#fff" stroke-width="0.9"/></svg>
        </span>
        www.tarvelpx.example
      </li>
    </ul>

    <svg class="swoosh" viewBox="0 0 520 70" preserveAspectRatio="none" aria-hidden="true">
      <defs>
        <linearGradient id="swooshFill" x1="0" y1="0" x2="1" y2="0">
          <stop offset="0" stop-color="#102a72"/>
          <stop offset="0.6" stop-color="#1d3f9e"/>
          <stop offset="1" stop-color="#2f6fe0"/>
        </linearGradient>
      </defs>
      <path d="M0 52 Q260 48 520 0 L520 70 L0 70 Z" fill="url(#swooshFill)"/>
      <path d="M0 46 Q260 42 520 -6" fill="none" stroke="#2f6fe0" stroke-width="1.5" opacity="0.6"/>
    </svg>
    <div class="swoosh__url">www.tarvelpx.example</div>
  </section>

</body>
</html>
```